Mirela Dawn Business Card Design

I need a business card for my daughter. She has it all described in the file below. But it needs to be square in shape. http://www.mireladawn.example is her web site

Target Market(s)

18-35 year old women

Industry/Entity Type

Fashion

Contact Information for Business Card

Please look at the attached file as it has all the details.

Requirements
Must have
• Please look at the attached file as it has all the details.
Nice to have
Should not have

```html
<!DOCTYPE html>
<html lang="en">
<head>
<meta charset="utf-8">
<title>Mirela Dawn — Business Card</title>
<link rel="stylesheet" href="https://fonts.googleapis.com/css2?family=Playfair+Display:wght@400;900&family=Dancing+Script:wght@500&display=swap">
<style>
  :root {
    --backdrop: #ecebea;
    --stone-dark: #0b0b0b;
    --stone-mid: #1c1c1a;
    --stone-vein: #4a463c;
    --blush: #cba3bd;
    --ink: #111111;
    --rule: #ffffff;
  }
  html, body {
    margin: 0;
    padding: 0;
    width: 1200px;
    height: 686px;
    overflow: hidden;
    background: var(--backdrop);
  }
  .stage {
    width: 1200px;
    height: 686px;
    display: flex;
    align-items: center;
    justify-content: center;
  }
  .card {
    position: relative;
    width: 640px;
    height: 640px;
    overflow: hidden;
  }
  .card__marble {
    position: absolute;
    inset: 0;
    background:
      linear-gradient(160deg, transparent 30%, var(--stone-vein) 33%, transparent 36%),
      linear-gradient(20deg, transparent 62%, var(--stone-vein) 64%, transparent 66%),
      linear-gradient(135deg, var(--stone-mid), var(--stone-dark) 55%, var(--stone-mid));
  }
  .card__panel {
    position: absolute;
    left: 60px;
    top: 140px;
    width: 520px;
    height: 360px;
    background: var(--blush);
    display: flex;
    flex-direction: column;
    align-items: center;
    justify-content: center;
    box-sizing: border-box;
    padding-top: 6px;
  }
  .card__name {
    margin: 0;
    font-family: "Playfair Display", "Bodoni Moda", serif;
    font-weight: 900;
    font-size: 52px;
    line-height: 1;
    letter-spacing: 3px;
    color: var(--ink);
    white-space: nowrap;
  }
  .card__rule {
    width: 330px;
    height: 5px;
    margin: 26px 0 22px;
    background: var(--rule);
  }
  .card__tagline {
    margin: 0;
    font-family: "Dancing Script", cursive;
    font-weight: 500;
    font-size: 38px;
    line-height: 1;
    color: var(--ink);
  }
  .card__website {
    margin: 30px 0 0;
    font-family: "Playfair Display", serif;
    font-weight: 400;
    font-size: 18px;
    line-height: 1;
    letter-spacing: 0.5px;
    color: var(--ink);
    white-space: nowrap;
  }
</style>
</head>
<body>
  <div class="stage">
    <main class="card">
      <div class="card__marble" role="img" aria-label="Black marble texture with cream veins"></div>
      <section class="card__panel">
        <h1 class="card__name">MIRELA DAWN</h1>
        <div class="card__rule"></div>
        <p class="card__tagline">fluent in fashion</p>
        <p class="card__website">http://www.mireladawn.example</p>
      </section>
    </main>
  </div>
</body>
</html>
```